Midnight Lanterns - Falling to Rise Reading the Hidden Grammar of Sleep

Book Title:
Midnight Lanterns
Falling to Rise

Reading the Hidden Grammar of Sleep

by Greta Vonhalm

tells the story of how dreams transform us, bringing the wisdom of our mind, body and spirit to us in our dreams. We have nerves coming into our brain from every part of our body relaying psychological and physiological information within us and it is revealed in our dream narrative.Once you understand the symbolic, visual language of dreams, you will find out/understand what is going on within. After all the dream is always about the dreamer. Yes, it is all about you!

Target Market(s)

Anyone who dreams, that includes all of us

Font styles to use
Serif

Colors
ec1f27
f37122
0692cd

Requirements
Must have
• Use this image please with Shadowed serif type font, in the color pallette
• I would like images for the cover to reflect being reborn for example - a phoenix. Dying in a dream is always a symbolic gesture/metaphor of profound psychological spiritual change, and the way the person dies is symbolic too. It's important that the image on the front reflects that.
Nice to have
• A good visual on the cover helps, just like they do in a dream since the language of the dream is symbols, metaphor, colors portray emotions. We respond to images because we only had images before our written language

```html
<!DOCTYPE html>
<html lang="en">
<head>
<meta charset="utf-8">
<title>Midnight Lanterns – Falling to Rise</title>
<link rel="stylesheet" href="https://fonts.googleapis.com/css2?family=Playfair+Display:wght@700;900&family=Lora:wght@400;600&display=swap">
<style>
  :root {
    --paper: #ece7d8;
    --red: #ec1f27;
    --orange: #f37122;
    --amber: #f6a13a;
    --gold: #f9c74f;
    --white: #ffffff;
    --shadow: rgba(120, 40, 10, 0.35);
  }
  * { margin: 0; padding: 0; box-sizing: border-box; }
  html, body {
    width: 800px;
    height: 1200px;
    overflow: hidden;
    background: var(--paper);
  }
  .cover {
    position: relative;
    width: 800px;
    height: 1200px;
    background: var(--paper);
    text-align: center;
  }
  .title {
    position: absolute;
    top: 22px;
    left: 0;
    width: 100%;
    font-family: "Playfair Display", Georgia, serif;
    font-weight: 900;
    color: var(--red);
    text-transform: uppercase;
    line-height: 1;
    text-shadow: 3px 3px 0 var(--shadow);
  }
  .title__line {
    display: block;
    font-size: 76px;
    letter-spacing: 1px;
  }
  .title__line + .title__line { margin-top: 6px; }
  .subtitle {
    position: absolute;
    top: 182px;
    left: 0;
    width: 100%;
    font-family: "Lora", Georgia, serif;
    font-weight: 400;
    font-size: 60px;
    color: var(--orange);
    line-height: 1;
    text-shadow: 2px 2px 0 var(--shadow);
  }
  .tagline {
    position: absolute;
    top: 278px;
    left: 0;
    width: 100%;
    font-family: "Lora", Georgia, serif;
    font-weight: 600;
    font-size: 21px;
    color: var(--white);
    text-shadow: 1px 1px 2px rgba(90, 40, 10, 0.55);
  }
  .phoenix-art {
    position: absolute;
    top: 345px;
    left: 95px;
    width: 610px;
    height: 650px;
  }
  .author {
    position: absolute;
    top: 1082px;
    left: 0;
    width: 100%;
    font-family: "Playfair Display", Georgia, serif;
    font-weight: 700;
    font-size: 54px;
    color: var(--red);
    text-transform: uppercase;
    letter-spacing: 1px;
    text-shadow: 3px 3px 0 var(--shadow);
  }
</style>
</head>
<body>
  <main class="cover">
    <h1 class="title">
      <span class="title__line">Midnight</span>
      <span class="title__line">Lanterns</span>
    </h1>
    <p class="subtitle">Falling to Rise</p>
    <p class="tagline">Reading the Hidden Grammar of Sleep</p>

    <svg class="phoenix-art" viewBox="0 0 610 650" role="img" aria-label="Illustration of a phoenix with spread wings rising from a bonfire, surrounded by small floating flames">
      <defs>
        <radialGradient id="phoenix-glow" cx="50%" cy="55%" r="55%">
          <stop offset="0%" stop-color="#f9c74f"/>
          <stop offset="45%" stop-color="#f6a13a"/>
          <stop offset="80%" stop-color="#f37122" stop-opacity="0.75"/>
          <stop offset="100%" stop-color="#ece7d8" stop-opacity="0"/>
        </radialGradient>
      </defs>
      <rect width="610" height="650" fill="url(#phoenix-glow)"/>
    </svg>

    <p class="author">Greta Vonhalm</p>
  </main>
</body>
</html>
```